Mirela Hartsby ADHD coach needs a flyer

I need a flyer to be sent by email. the copy is attached. It can be changed/reduced to fit the flyer. I would like to keep my website colors. My website is www.mirelahartsby.example - Thank you!

```html
<!DOCTYPE html>
<html lang="en">
<head>
<meta charset="utf-8">
<title>Mirela Hartsby – ADHD and Academic Coach Flyer</title>
<link rel="stylesheet" href="https://fonts.googleapis.com/css2?family=Nunito+Sans:ital,wght@0,700;0,800;0,900;1,400&family=Jost:ital,wght@0,300;0,400;0,600;1,300;1,400&family=Oswald:wght@200;300&display=swap">
<style>
  :root {
    --stage: #1f1f21;
    --paper: #ffffff;
    --brand-blue: #9bb5c0;
    --name-blue: #93aebb;
    --ink: #2c3136;
    --ink-soft: #3f454a;
    --sub-ink: #333e45;
    --charcoal: #666666;
    --rule: #9bb5c0;
  }
  * { box-sizing: border-box; margin: 0; padding: 0; }
  html, body { width: 1200px; height: 960px; overflow: hidden; background: var(--stage); }
  body { position: relative; font-family: "Jost", sans-serif; color: var(--ink); }

  .page {
    position: absolute; top: 141px; width: 518px; height: 670px;
    background: var(--paper); overflow: hidden;
  }
  .page--front { left: 65px; }
  .page--back { left: 617px; }

  /* front */
  .hero-photo {
    position: absolute; left: 0; top: 0; width: 518px; height: 316px;
    background: linear-gradient(90deg, #a1b0b4 0%, #9aaaae 55%, #b3bcbd 75%, #a2b0b3 100%);
  }
  .hero-frame {
    position: absolute; left: 29px; top: 29px; width: 483px; height: 287px;
    border: 1px solid rgba(255,255,255,0.85); border-bottom: none;
  }
  .hero-title {
    position: absolute; left: 43px; top: 72px; width: 260px;
    font-family: "Nunito Sans", sans-serif; font-weight: 900;
    font-size: 19.5px; line-height: 24.4px; color: #fff; letter-spacing: 0.2px; white-space: nowrap;
  }
  .hero-sub {
    position: absolute; left: 43px; top: 218px; width: 220px;
    font-family: "Nunito Sans", sans-serif; font-weight: 800;
    font-size: 11px; line-height: 14.4px; color: var(--sub-ink); white-space: nowrap;
  }
  .intro {
    position: absolute; left: 43px; top: 328px; width: 200px;
    font-size: 8.7px; line-height: 11.2px; font-weight: 400; color: var(--ink-soft);
  }
  .intro p + p { margin-top: 11.2px; }
  .brand-name {
    position: absolute; left: 306px; top: 324px;
    font-family: "Oswald", sans-serif; font-weight: 200;
    font-size: 55px; line-height: 52px; color: var(--name-blue); letter-spacing: 0.5px;
  }
  .brand-rule {
    position: absolute; left: 268px; top: 437px; width: 250px; height: 1px; background: var(--rule);
  }
  .brand-title {
    position: absolute; left: 308px; top: 447px;
    font-family: "Oswald", sans-serif; font-weight: 300; font-size: 13px; color: var(--ink-soft);
  }
  .group-photo {
    position: absolute; left: 268px; top: 476px; width: 250px; height: 149px;
    background: linear-gradient(180deg, #c9dca8 0%, #8fae72 40%, #a58365 78%, #7d5a40 100%);
  }
  .footer {
    position: absolute; left: 0; bottom: 0; width: 518px; height: 28px;
    display: flex; align-items: center; justify-content: center;
    font-size: 11px; font-weight: 300; color: #fff;
  }
  .footer--blue { background: var(--brand-blue); }
  .footer--gray { background: var(--charcoal); }

  /* back */
  .sidebar {
    position: absolute; left: 0; top: 0; width: 182px; height: 400px;
    background: linear-gradient(180deg, #9db7c3 0%, #b5cad3 45%, #e6eef1 80%, #ffffff 100%);
  }
  .col { position: absolute; font-size: 7.9px; font-weight: 400; color: var(--ink); }
  .col--focus { left: 28px; top: 31px; width: 142px; line-height: 10.1px; }
  .col--results { left: 202px; top: 31px; width: 284px; line-height: 9.6px; }
  .section-head {
    font-family: "Nunito Sans", sans-serif; font-weight: 900; font-size: 12px; line-height: 14px; color: #1f2326;
  }
  .section-kicker { font-style: italic; font-weight: 400; font-size: 11.5px; line-height: 14px; margin-bottom: 2px; color: #2a2e31; }
  .col--focus p + p { margin-top: 10px; }
  .bullets { list-style: none; }
  .bullets li { position: relative; padding-left: 13px; }
  .bullets li::before { content: ""; position: absolute; left: 1px; top: 3.5px; width: 3px; height: 3px; border-radius: 50%; background: #222; }
  .col--focus .bullets li { margin-bottom: 3px; }
  .sub-head {
    font-family: "Nunito Sans", sans-serif; font-weight: 800; font-size: 11.5px; line-height: 14px;
    margin-top: 8px; margin-bottom: 2px; color: #1f2326;
  }
  .sub-head--parents { margin-top: 10px; }
  .quote { font-size: 7.4px; line-height: 9.6px; }
  .quote + .quote { margin-top: 5px; }
  .quote em { font-style: italic; }
  .next-steps {
    width: 287px; height: 49px; margin-top: 5px;
    background: var(--charcoal); color: #fff; padding: 6px 14px;
  }
  .next-steps h3 { font-family: "Nunito Sans", sans-serif; font-weight: 800; font-size: 11.5px; line-height: 13px; }
  .next-steps p { font-size: 8.4px; line-height: 11px; font-weight: 300; }
  .next-steps strong { font-weight: 600; }
  .team-photo {
    position: absolute; left: 0; top: 396px; width: 518px; height: 246px;
    background: linear-gradient(180deg, #e9ecec 0%, #cfd3d4 35%, #b7a696 70%, #8d8f9a 100%);
  }
</style>
</head>
<body>

<section class="page page--front">
  <div class="hero-photo" role="img" aria-label="Portrait photo of the coach smiling with arms crossed against a grey wall"></div>
  <div class="hero-frame"></div>
  <h1 class="hero-title">Helping Your Child<br>with ADHD or Other<br>Learning Challenges<br>Thrive in College<br>and Beyond</h1>
  <p class="hero-sub">Academic success coaching that<br>leads to lifelong transformation<br>for students with ADHD and<br>similar challenges that may<br>have impeded their ability to<br>thrive.</p>

  <div class="intro">
    <p>Sending your child off to college can feel scary, especially if that college is hundreds of miles away. You worry about how they'll do on their own—whether they'll make friends, earn good grades, and be happy—especially without you there to support them daily. You know your child is bright, and you want them to have a great future, but you're concerned they will struggle without the right support and resources.</p>
    <p>You don't need to feel helpless as you send your child off to this next stage of their lives. Mirela is dedicated to making that transition easier for everyone. Mirela Hartsby has years of experience helping students thrive despite their challenges. She sees your child's potential and helps them see it, too. She provides a safety net as they adjust to a new environment at college. Her services are comprehensive and adaptable, based on the requirements of each individual: helping with course selection and scheduling, time management, study strategies, focus, making new friends, and adapting to change. Through it all, Mirela guides students through fundamental work on mindset to ensure that changes stick.</p>
  </div>

  <div class="brand-name">MIRELA<br>HARTSBY</div>
  <div class="brand-rule"></div>
  <div class="brand-title">Ph.D. &nbsp;|&nbsp; ADHD and Academic Coach</div>
  <div class="group-photo" role="img" aria-label="Photo of a group of college students sitting together outdoors with laptops and tablets"></div>

  <footer class="footer footer--blue">www.mirelahartsby.example</footer>
</section>

<section class="page page--back">
  <div class="sidebar"></div>

  <div class="col col--focus">
    <h2 class="section-head">EMPOWERING FOCUS:</h2>
    <p class="section-kicker">HOW MIRELA HELPS</p>
    <p>Mirela has taken students from failing to a 3.0 GPA, and from a C student to the Dean's List, in just one semester. It doesn't take years to provide lasting results; all it takes is the right guide.</p>
    <p>Uniquely positioned to help your child, Mirela:</p>
    <ul class="bullets">
      <li>Tailors support so that your child improves focus and maximizes their potential in college and beyond.</li>
      <li>Understands your child's unique needs - she sees the gifts that others often miss.</li>
      <li>Knows the academic landscape intimately, including the challenges faced by students with ADHD and other conditions.</li>
      <li>Helps with the logistics of scheduling in a way that most advisors can't, enrolling students in the courses that best suit their learning style.</li>
      <li>Nurtures the brilliance in your bright child.</li>
      <li>Provides a balance between encouraging students and challenging them.</li>
    </ul>
  </div>

  <div class="col col--results">
    <h2 class="section-head">REALIZING POTENTIAL:</h2>
    <p class="section-kicker">THE TRANSFORMATION YOU'LL SEE IN YOUR CHILD</p>
    <ul class="bullets">
      <li>A mindset of self-belief and increased confidence.</li>
      <li>Higher grades and the drive to graduate.</li>
      <li>Social integration and making friends.</li>
      <li>Happiness and fulfilment.</li>
      <li>A deep sense of personal achievement and pride.</li>
    </ul>

    <h3 class="sub-head">You Will Have:</h3>
    <ul class="bullets">
      <li>Less stress, knowing that your child is in good hands.</li>
      <li>Fewer sleepless nights worrying about your child.</li>
      <li>Confidence that they are receiving the right support.</li>
      <li>Joy and pride at seeing them do well.</li>
    </ul>

    <h3 class="sub-head sub-head--parents">What Parents Say</h3>
    <p class="quote">"Mirela was the glue that kept our daughter in college… as our daughter's Academic Coach, [she] gave our daughter the ability to finish strong by empowering her with the skills needed to be successful."—<em>Renata</em></p>
    <p class="quote">"Mirela has always told my daughter not that she can succeed, but that she <em>will</em> succeed."—<em>Colleen</em></p>

    <h3 class="sub-head">What Students Say</h3>
    <p class="quote"><em>"Last semester I completed all 16 hours and I had the highest GPA I've ever had!"<br>—Former student</em></p>
    <p class="quote">"Under her instruction, my grades began to improve. I ended up making the Dean's List during my time at Ridgefield, and I was also inducted into Sigma Tau Rho. I am currently in my first year of law school at Harlow State University, a top tier school."—<em>Former student</em></p>

    <div class="next-steps">
      <h3>Next Steps</h3>
      <p>To learn more and discuss your child's individual needs, call<br><strong>555·013·0142</strong> or email <strong>coach@mirelahartsby.example</strong></p>
    </div>
  </div>

  <div class="team-photo" role="img" aria-label="Photo of four students working together over papers at a table"></div>

  <footer class="footer footer--gray">www.mirelahartsby.example</footer>
</section>

</body>
</html>
```